Lantern of the Meadow website design

To create 2 pages (a front page and sub page) for a health/spiritual website. I have a logo, and was thinking of incorporating Greek temple columns in the design or something similar, but open to other ideas.

The design should suit mobile devices with limited screen space also.

Industry/Entity Type

Health

Number of Pages Required

1 page

```html
<!DOCTYPE html>
<html lang="en">
<head>
<meta charset="utf-8">
<title>Lantern of the Meadow</title>
<link rel="stylesheet" href="https://fonts.googleapis.com/css2?family=Lato:wght@400;700;900&display=swap">
<style>
:root{
  --blue:#13a6e6;
  --blue-deep:#1e8fc5;
  --navy:#16263a;
  --ink:#2f3438;
  --grey:#7d8388;
  --white:#ffffff;
  --footer:#383e3a;
  --footer-bar:#2a2e2c;
  --footer-text:#b9bfba;
}
*{box-sizing:border-box;margin:0;padding:0}
html,body{width:1200px;height:2956px;overflow:hidden}
body{font-family:'Lato',sans-serif;color:var(--ink);background:var(--white)}
.page{position:relative;width:1200px;height:2956px;overflow:hidden}
.abs{position:absolute}

/* hero */
.hero{left:0;top:0;width:1200px;height:802px;
  background:
    radial-gradient(ellipse 900px 260px at 70% 330px,rgba(120,125,132,.55) 0%,rgba(120,125,132,0) 70%),
    radial-gradient(ellipse 520px 420px at 260px 640px,rgba(8,8,8,.85) 0%,rgba(8,8,8,0) 75%),
    linear-gradient(180deg,#2d2a26 0%,#4c4436 7%,#6a5a42 12%,#4f4d4a 18%,#55585c 30%,#4a4d51 45%,#34373a 60%,#1f2021 78%,#141414 100%)}
.brand{left:160px;top:44px;display:flex;align-items:center;gap:14px;color:var(--white);font-weight:700;font-size:15px}
.brand-dot{width:62px;height:62px;border-radius:50%;background:#b9bcbf}
.nav{left:489px;top:50px;font-size:13px;font-weight:700;letter-spacing:.6px}
.nav a{position:absolute;white-space:nowrap;color:var(--white);text-decoration:none}
.nav a.active{border-bottom:2px solid var(--blue);padding-bottom:7px}
.hero-title{left:540px;top:244px;width:500px;text-align:right;color:var(--blue);font-weight:900;font-size:26px;line-height:32px;letter-spacing:.8px}
.hero-text{left:548px;top:338px;width:492px;text-align:right;color:#e4e4e4;font-size:13.5px;line-height:16.5px}
.btn{display:flex;align-items:center;justify-content:center;border-radius:30px;font-weight:700;letter-spacing:.6px}
.btn-hero{left:908px;top:463px;width:130px;height:39px;background:var(--blue);color:var(--white);font-size:11.5px}

/* about */
.about-icon{left:232px;top:884px}
.about-title{left:286px;top:885px;font-size:28px;font-weight:700;letter-spacing:1.5px;color:var(--ink)}
.about-rule{left:232px;top:925px;width:172px;height:2px;background:var(--blue)}
.about-text{left:232px;width:358px;font-size:13.5px;line-height:16.5px;color:var(--grey)}
.about-art{left:659px;top:858px;width:380px;height:380px;border-radius:50%;
  background:radial-gradient(circle,rgba(19,166,230,.45) 0%,rgba(19,166,230,.28) 30%,rgba(19,166,230,.5) 45%,rgba(19,166,230,.25) 70%,rgba(255,255,255,0) 100%)}

/* foundations */
.foundations{left:0;top:1275px;width:1200px;height:447px;
  background:radial-gradient(circle at 20% 35%,#2c3b6a 0%,transparent 30%),radial-gradient(circle at 80% 60%,#0f4a70 0%,transparent 35%),linear-gradient(135deg,#1d2c4c 0%,#0c3150 55%,#0a3a5c 100%)}
.found-title{left:0;top:1316px;width:1200px;text-align:center;color:var(--white);font-size:27px;letter-spacing:2px;font-weight:400}
.found-text{left:305px;top:1391px;width:632px;text-align:center;color:var(--white);font-size:14px;line-height:31px;font-weight:700}
.btn-found{left:504px;top:1621px;width:191px;height:59px;background:var(--white);color:var(--ink);font-size:14px}

/* services */
.svc-title{left:0;top:1770px;width:1200px;text-align:center;font-size:29px;letter-spacing:2px;color:var(--ink);font-weight:400}
.svc-intro{left:187px;top:1838px;width:827px;text-align:center;font-size:10.5px;line-height:14px;color:var(--ink)}
.svc-tile{top:1901px;width:197px;height:197px;box-shadow:0 3px 8px rgba(0,0,0,.25)}
.tile-dark{background:radial-gradient(circle,#24374d 0%,var(--navy) 60%)}
.tile-blue{background:radial-gradient(circle,#3aa6d8 0%,var(--blue-deep) 60%)}
.svc-name{top:2120px;width:280px;text-align:center;font-size:18px;font-weight:700;letter-spacing:1.5px;color:var(--ink)}
.svc-text{top:2162px;width:240px;text-align:center;font-size:13.5px;line-height:16px;color:var(--grey)}

/* contact */
.contact{left:0;top:2256px;width:1200px;height:506px;
  background:linear-gradient(180deg,#3c3c3f 0%,#4b4a4c 25%,#2e3035 50%,#1f2226 75%,#1b1d20 100%)}
.contact-title{left:0;top:2294px;width:1200px;text-align:center;color:var(--blue);font-size:24px;font-weight:700;letter-spacing:1.2px}
.contact-text{left:370px;top:2344px;width:460px;text-align:center;color:#d3d5d7;font-size:13.5px;line-height:17px}
.field{border:1.5px solid var(--blue-deep);background:transparent}
.btn-submit{left:504px;top:2665px;width:191px;height:63px;background:var(--blue);color:var(--white);font-size:18px;letter-spacing:1.5px}

/* footer */
.footer{left:0;top:2762px;width:1200px;height:144px;background:var(--footer)}
.footer-dot{left:216px;top:2780px;width:50px;height:50px;border-radius:50%;background:#b9bcbf}
.footer-brand{left:166px;top:2840px;width:150px;text-align:center;color:#d4d6d8;font-weight:700;font-size:12px;line-height:15px}
.footer-col{top:2778px;font-size:12.5px;line-height:16.4px;color:var(--footer-text)}
.footer-col h4{color:var(--white);font-size:13px;letter-spacing:1px;font-weight:700;margin-bottom:15px}
.footer-bar{left:0;top:2906px;width:1200px;height:50px;background:var(--footer-bar)}
.copyright{left:177px;top:2923px;font-size:13px;color:var(--footer-text)}
.copyright u{text-decoration:underline}
.social{top:2917px;width:28px;height:28px;border-radius:50%;background:#6c716e}
</style>
</head>
<body>
<div class="page">

  <section class="abs hero" role="img" aria-label="Photograph of a person sitting on a rock above a sea of clouds at dusk"></section>

  <div class="abs brand"><span class="brand-dot"></span>Lantern of the Meadow</div>
  <nav class="abs nav">
    <a class="active" style="left:0">HOME</a>
    <a style="left:78px">ABOUT US</a>
    <a style="left:183px">FOUNDATIONS PROGRAM</a>
    <a style="left:389px">SERVICES</a>
    <a style="left:486px">CONTACT</a>
  </nav>

  <h1 class="abs hero-title">SPIRITUAL TITLE CAN BE PLACED HERE</h1>
  <p class="abs hero-text">Lorem ipsum dolor sit amet, consectetur adipisicing elit, sed do eiusmod tempor incididunt ut labore et dolore magna aliqua. Ut enim ad minim veniam, quis nostrud exercitation ullamco laboris nisi ut aliquip ex ea commodo consequat.</p>
  <div class="abs btn btn-hero">LEARN MORE</div>

  <svg class="abs about-icon" width="34" height="36" viewBox="0 0 34 36" aria-hidden="true">
    <rect x="1" y="2" width="32" height="5" fill="#13a6e6"/>
    <rect x="5" y="9" width="5" height="21" fill="#13a6e6"/>
    <rect x="14.5" y="9" width="5" height="21" fill="#13a6e6"/>
    <rect x="24" y="9" width="5" height="21" fill="#13a6e6"/>
    <rect x="1" y="31" width="32" height="4" fill="#13a6e6"/>
  </svg>
  <h2 class="abs about-title">ABOUT US</h2>
  <div class="abs about-rule"></div>
  <p class="abs about-text" style="top:968px">Lorem ipsum dolor sit amet, consectetur adipisicing elit, sed do eiusmod tempor incididunt ut labore et dolore magna aliqua.</p>
  <p class="abs about-text" style="top:1036px">Ut enim ad minim veniam, quis nostrud exercitation ullamco laboris nisi ut aliquip ex ea commodo consequat.</p>
  <p class="abs about-text" style="top:1102px">Lorem ipsum dolor sit amet, consectetur adipisicing elit, sed do eiusmod tempor incididunt ut labore et dolore magna aliqua. Ut enim ad minim veniam, quis nostrud exerc.</p>
  <div class="abs about-art" role="img" aria-label="Illustration of a meditating figure surrounded by radiating blue rays"></div>

  <section class="abs foundations" role="img" aria-label="Deep blue background with soft glowing light spots and a faint meditating figure"></section>
  <h2 class="abs found-title">THE FOUNDATIONS PROGRAM</h2>
  <p class="abs found-text">Lorem ipsum dolor sit amet, consectetur adipisicing elit, sed do eiusmod tempor incididunt ut labore et dolore magna aliqua. Ut enim ad minim veniam, quis nostrud exercitation ullamco laboris nisi ut aliquip ex ea commodo consequat. Duis aute irure dolor in reprehenderit in voluptate velit esse cillum dolore eu fugiat nulla pariatur. Excepteur sint occaecat cupidatat non proident, sunt in culpa qui officia deserunt mollit anim id est laborum. Sed ut perspiciatis unde omnis iste natus error sit voluptatem accusantium</p>
  <div class="abs btn btn-found">LEARN MORE TODAY</div>

  <h2 class="abs svc-title">WE OFFER THIS SERVICES</h2>
  <p class="abs svc-intro">Lorem ipsum dolor sit amet, consectetur adipisicing elit, sed do eiusmod tempor incididunt ut labore et dolore magna aliqua. Ut enim ad minim veniam, quis nostrud exercitation ullamco laboris nisi ut aliquip ex ea commodo consequat.</p>

  <div class="abs svc-tile tile-dark" style="left:217px" role="img" aria-label="Line icon of a figure seated in meditation"></div>
  <div class="abs svc-tile tile-blue" style="left:502px" role="img" aria-label="Line icon of a lotus flower"></div>
  <div class="abs svc-tile tile-dark" style="left:786px" role="img" aria-label="Line icon of a meditating figure with a radiant halo"></div>

  <h3 class="abs svc-name" style="left:176px">SERVICE #1</h3>
  <h3 class="abs svc-name" style="left:460px">SERVICE #2</h3>
  <h3 class="abs svc-name" style="left:745px">SERVICE #3</h3>
  <p class="abs svc-text" style="left:196px">Ad minim veniam, quis nostrud exercitation ullamco laboris nisi ut aliquip ex ea commodo consequat.</p>
  <p class="abs svc-text" style="left:480px">Ad minim veniam, quis nostrud exercitation ullamco laboris nisi ut aliquip ex ea commodo consequat.</p>
  <p class="abs svc-text" style="left:765px">Ad minim veniam, quis nostrud exercitation ullamco laboris nisi ut aliquip ex ea commodo consequat.</p>

  <section class="abs contact" role="img" aria-label="Dusk photograph of a long bridge over calm water"></section>
  <h2 class="abs contact-title">CONTACT US TODAY</h2>
  <p class="abs contact-text">Ad minim veniam, quis nostrud exercitation ullamco laboris nisi ut aliquip ex ea commodo consequat.</p>
  <div class="abs field" style="left:264px;top:2425px;width:323px;height:47px"></div>
  <div class="abs field" style="left:613px;top:2425px;width:323px;height:47px"></div>
  <div class="abs field" style="left:264px;top:2496px;width:672px;height:142px"></div>
  <div class="abs btn btn-submit">SUBMIT</div>

  <footer class="abs footer"></footer>
  <span class="abs footer-dot"></span>
  <div class="abs footer-brand">Lantern of the Meadow</div>
  <div class="abs footer-col" style="left:406px"><h4>SERVICES</h4>Service 1<br>Service 2<br>Service 3<br>Services Page<br>Spiritual Guidance</div>
  <div class="abs footer-col" style="left:591px"><h4>RESOURCES</h4>Features<br>Inspiration Center<br>Success Stories<br>Spiritual Guidance<br>Developer Docs</div>
  <div class="abs footer-col" style="left:772px"><h4>SUPPORT</h4>Support Center<br>Community</div>
  <div class="abs footer-col" style="left:932px"><h4>PARTNERS</h4>Affiliates<br>Desiggners<br>Developers<br>Education</div>

  <div class="abs footer-bar"></div>
  <p class="abs copyright">© Lantern of the Meadow, Inc. <u>Mind</u>, <u>Body</u>, <u>Spirit</u></p>
  <span class="abs social" style="left:800px"></span>
  <span class="abs social" style="left:843px"></span>
  <span class="abs social" style="left:886px"></span>
  <span class="abs social" style="left:930px"></span>
  <span class="abs social" style="left:973px"></span>

</div>
</body>
</html>
```